Brightvale Energy International Website

Brightvale Energy – Lighting the Path of
UK Homes Sustainably.

New Launch Website

Focus on 4 Product Categories

- Solar PV
- Battery Energy Storage
- EV Charging
- Heat Pumps

Add

Energy News
Enquire Now button Top right every page
Contact us page

Follow Lumenhaus.co.uk for similar content pages

Target Market(s)

Residential home owners UK NOT US

Industry/Entity Type

Solar energy, home energy , EV charging

Coding

Coded - Design and coding required

Number of Pages Required

5+ page

Font styles to use
Sans Serif

Colors
0054AA
0677BA
7BADD7
CADEEF
E8F1F8
59FF00
82FF00
B8FF75
E3FFCB
F4FFEA
FFF300
FFF600
FEFA6F
FFFEC7
FFFEE8

Requirements
Must have
• Strong brand logo on every page, clear content bar
Nice to have
• Add these logos from LumenHaus.co.uk

```html
<!DOCTYPE html>
<html lang="en">
<head>
<meta charset="UTF-8">
<title>Brightvale Energy – Lighting the Path of UK Homes Sustainably</title>
<link href="https://fonts.googleapis.com/css2?family=Poppins:wght@400;500;600;700&display=swap" rel="stylesheet">
<style>
:root{
  --green-dark:#173f2b;
  --green-deep:#0f3321;
  --green:#2f6b45;
  --green-accent:#5dae3a;
  --lime:#9be15d;
  --yellow:#f4d03f;
  --ink:#1c2a22;
  --muted:#5d6b63;
  --line:#e3e9e5;
  --sky:#e8f1f8;
  --white:#ffffff;
}
*{box-sizing:border-box;margin:0;padding:0}
html,body{width:1200px;height:5280px;overflow:hidden}
body{font-family:'Poppins',sans-serif;color:var(--ink);background:var(--white);position:relative;font-size:13px;line-height:1.55}
.abs{position:absolute}
.btn{display:inline-block;border-radius:22px;padding:10px 22px;font-size:12px;font-weight:600;text-decoration:none}
.btn-dark{background:var(--green-dark);color:var(--white)}
.btn-light{background:var(--white);color:var(--green-dark);border:1px solid var(--line)}
.btn-lime{background:var(--lime);color:var(--green-deep)}
.logo{display:flex;align-items:center;gap:8px;font-weight:700;font-size:20px;color:var(--green-dark)}
.logo .dot{width:22px;height:22px;border-radius:50%;background:var(--yellow)}
.photo{border-radius:14px}
h2.section-title{font-size:34px;font-weight:700;text-align:center;line-height:1.25;color:var(--ink)}
.tick{display:inline-flex;width:14px;height:14px;border-radius:50%;background:var(--green-accent);margin-right:8px;vertical-align:-2px;align-items:center;justify-content:center}
.tick svg{width:8px;height:8px}

/* top bar */
.topbar{top:0;left:0;width:1200px;height:40px;background:var(--green-dark);color:#d8e6dd;font-size:11px;display:flex;align-items:center;padding:0 40px;gap:28px}
.topbar .socials{margin-left:auto;display:flex;gap:8px}
.topbar .socials span{width:14px;height:14px;border-radius:50%;background:#3c6b50}

/* nav */
.nav{top:40px;left:0;width:1200px;height:80px;display:flex;align-items:center;padding:0 40px;background:var(--white)}
.nav ul{list-style:none;display:flex;gap:30px;margin-left:90px;font-size:13px;font-weight:500}
.nav .actions{margin-left:auto;display:flex;gap:10px}

/* hero */
.hero{top:120px;left:0;width:1200px;height:600px;background:linear-gradient(180deg,#f5faf3,#ffffff)}
.hero-photo{right:0;top:0;width:780px;height:600px;background:linear-gradient(90deg,#f5faf3 0%,#c9ddd0 25%,#7ea0b8 55%,#4d6f8c 80%,#f2c879 100%)}
.hero-text{left:40px;top:70px;width:460px}
.hero-text h1{font-size:52px;line-height:1.15;font-weight:700;color:var(--ink)}
.hero-text h1 em{font-style:normal;color:var(--green)}
.hero-text p{margin:22px 0 26px;color:var(--muted);font-size:13px}
.hero-stats{left:40px;top:455px;display:flex;gap:10px}
.stat-card{background:var(--white);border-radius:10px;padding:12px 18px;box-shadow:0 4px 14px rgba(0,0,0,.07);min-width:120px}
.stat-card b{display:block;font-size:20px;color:var(--green-dark)}
.stat-card span{font-size:11px;color:var(--muted)}

/* about */
.about{top:740px;left:0;width:1200px;height:460px}
.about-text{left:40px;top:20px;width:520px}
.about-text h2{font-size:36px;font-weight:700;margin-bottom:16px}
.about-text h3{font-size:20px;color:var(--green);margin:18px 0 8px}
.about-text p{color:var(--muted);font-size:12.5px;margin-bottom:18px}
.about-photo{left:620px;top:40px;width:540px;height:340px;background:linear-gradient(160deg,#dfe8ee,#8fa9bd 50%,#3e5a6f)}
.badge{left:590px;top:300px;background:var(--white);border-radius:12px;padding:14px 18px;box-shadow:0 6px 18px rgba(0,0,0,.12);display:flex;gap:18px;align-items:center}
.badge small{display:block;font-size:11px;color:var(--muted)}
.badge b{font-size:20px}
.badge i{width:34px;height:34px;border-radius:50%;background:var(--yellow);display:block}

/* solutions */
.solutions{top:1210px;left:0;width:1200px;height:650px}
.cards{left:80px;top:110px;display:flex;gap:20px}
.sol-card{width:245px}
.sol-card .img{height:190px;border-radius:10px}
.sol-card h3{font-size:18px;margin:16px 0 8px}
.sol-card p{font-size:11.5px;color:var(--muted);margin-bottom:12px}
.sol-card li{list-style:none;font-size:11.5px;margin-bottom:6px}
.sol-card .btn{margin-top:12px}

/* certified */
.certified{top:1920px;left:0;width:1200px;height:520px;background:var(--green-deep);color:var(--white);text-align:center}
.certified h2{font-size:34px;margin-top:70px}
.certified p.lead{width:700px;margin:12px auto 32px;color:#b9cfc1;font-size:12.5px}
.chips{display:grid;grid-template-columns:repeat(3,250px);gap:14px 20px;justify-content:center}
.chip{background:#245238;border-radius:6px;padding:10px 14px;font-size:11.5px;text-align:left;display:flex;gap:10px;align-items:center}
.chip i{width:14px;height:14px;background:var(--lime);border-radius:3px;flex:none}
.certified h4{margin-top:36px;font-size:16px;font-weight:600}
.certified h4 em{font-style:normal;color:var(--lime)}
.certified .btn{margin-top:18px}

/* values */
.values{top:2460px;left:0;width:1200px;height:360px}
.value-cards{left:80px;top:100px;display:flex;gap:20px}
.value{width:245px;height:220px;border:1px solid var(--line);border-radius:12px;text-align:center;padding:26px 20px;box-shadow:0 4px 14px rgba(0,0,0,.04)}
.value i{display:block;width:46px;height:46px;border-radius:50%;background:#e6f3dc;margin:0 auto 14px}
.value h3{font-size:16px;margin-bottom:8px}
.value p{font-size:11.5px;color:var(--muted)}

/* why */
.why{top:2840px;left:0;width:1200px;height:400px;background:linear-gradient(90deg,#ffffff,var(--sky) 40%,#dce9f3)}
.why-photo-a{left:80px;top:30px;width:300px;height:220px;background:linear-gradient(150deg,#cfdbe6,#6f8ea8)}
.why-photo-b{left:200px;top:160px;width:300px;height:210px;background:linear-gradient(150deg,#f4d58d,#6a8f5d)}
.savings{left:100px;top:290px;background:var(--white);border-radius:10px;padding:10px 16px;box-shadow:0 6px 16px rgba(0,0,0,.1)}
.savings small{display:block;font-size:11px;color:var(--muted)}
.savings b{font-size:18px}
.why-text{left:600px;top:40px;width:520px}
.why-text h2{font-size:34px;margin-bottom:12px}
.why-text p{font-size:12px;color:var(--muted);margin-bottom:16px}
.why-text li{list-style:none;font-size:12.5px;margin-bottom:10px;font-weight:500}

/* news */
.news{top:3320px;left:0;width:1200px;height:720px}
.news h2{left:40px;top:20px;font-size:36px}
.news .intro{left:760px;top:10px;width:380px;font-size:12px;color:var(--muted)}
.news-cards{left:40px;top:110px;display:flex;gap:20px}
.news-card{width:265px}
.news-card .img{height:200px;border-radius:10px}
.news-card .date{font-size:10.5px;color:var(--muted);margin:12px 0 4px}
.news-card h3{font-size:14.5px;line-height:1.35;margin-bottom:8px}
.news-card p{font-size:11.5px;color:var(--muted);margin-bottom:10px}
.news-card a{font-size:11.5px;color:var(--green);font-weight:600;text-decoration:underline}
.pager{left:560px;top:640px;display:flex;gap:10px}
.pager span{width:34px;height:34px;border-radius:50%;display:flex;align-items:center;justify-content:center;border:1px solid var(--line)}
.pager span.on{background:var(--green-dark);border-color:var(--green-dark)}

/* cta */
.cta{top:4120px;left:0;width:1200px;height:840px;background:linear-gradient(180deg,#ffffff 0%,#e6eef2 20%,#a8bfc8 45%,#4f7a5e 75%,#2c5a3a 100%)}
.cta h2{top:80px;width:1200px;text-align:center;font-size:38px}
.cta .lead{top:140px;left:380px;width:440px;text-align:center;font-size:12px;color:var(--muted)}
.contact-panel{left:150px;top:240px;width:400px;height:430px;background:rgba(15,51,33,.55);border-radius:14px;padding:30px;color:var(--white)}
.contact-item{display:flex;gap:14px;margin-bottom:28px}
.contact-item i{width:32px;height:32px;border-radius:8px;background:rgba(255,255,255,.15);flex:none;display:flex;align-items:center;justify-content:center}
.contact-item b{display:block;font-size:14px}
.contact-item span{font-size:12px;color:#d6e4da}
.quote{left:580px;top:240px;width:470px;height:430px;background:var(--green-dark);border-radius:14px;padding:30px;color:var(--white)}
.quote h3{font-size:22px}
.quote .sub{font-size:11.5px;color:#b9cfc1;margin:4px 0 20px}
.quote-row{display:flex;justify-content:space-between;background:var(--white);color:var(--ink);border-radius:6px;padding:12px 14px;font-size:12px;margin-bottom:12px}
.quote-row b{color:var(--green)}
.quote .btn{display:block;text-align:center;margin-top:20px;background:var(--white);color:var(--green-dark);border-radius:6px}
.quote .rating{margin-top:16px;font-size:11px;text-align:center;color:#d6e4da}
.quote .rating em{font-style:normal;color:var(--yellow)}

/* stats bar */
.statsbar{top:4960px;left:0;width:1200px;height:70px;background:var(--green-deep);display:flex;justify-content:space-around;align-items:center;color:var(--white);text-align:center;border-bottom:1px solid #2b5a40}
.statsbar b{display:block;font-size:20px}
.statsbar span{font-size:11px;color:#b9cfc1}

/* footer */
.footer{top:5030px;left:0;width:1200px;height:250px;background:var(--green-deep);color:#c6d8cc}
.footer .logo{color:var(--white)}
.footer-brand{left:40px;top:30px;width:300px}
.footer-brand p{font-size:11px;margin:12px 0}
.footer-brand .soc{display:flex;gap:8px}
.footer-brand .soc span{width:18px;height:18px;border-radius:50%;background:#2f5e44}
.footer-cols{left:500px;top:30px;display:flex;gap:70px}
.footer-cols h4{color:var(--white);font-size:13px;margin-bottom:10px}
.footer-cols li{list-style:none;font-size:11px;margin-bottom:5px}
.footer-bottom{left:40px;top:200px;width:1120px;border-top:1px solid #2b5a40;padding-top:14px;display:flex;justify-content:space-between;font-size:10.5px}
</style>
</head>
<body>

<div class="abs topbar">
  <span>0800 046 2817</span>
  <span>hello@brightvaleenergy.co.uk</span>
  <span>12 Harbour Row, Kelston</span>
  <div class="socials"><span></span><span></span><span></span><span></span></div>
</div>

<header class="abs nav">
  <div class="logo"><span class="dot"></span>Brightvale Energy</div>
  <ul><li>Home</li><li>About Us</li><li>Products</li><li>Energy News</li><li>Contact</li></ul>
  <div class="actions"><a class="btn btn-light">Contact Us</a><a class="btn btn-dark">Enquire Now</a></div>
</header>

<section class="abs hero">
  <div class="abs hero-photo" role="img" aria-label="Rooftop solar panels on UK homes at sunset"></div>
  <div class="abs hero-text">
    <h1>Powering the Future of <em>UK Homes</em> Sustainably.</h1>
    <p>Transform your home into a sustainable energy powerhouse with our cutting-edge solar solutions, battery storage, and renewable energy systems. Join thousands of UK homeowners reducing their carbon footprint while saving on energy costs.</p>
    <a class="btn btn-dark">Enquire Now</a>&nbsp; <a class="btn btn-light">Learn More</a>
  </div>
  <div class="abs hero-stats">
    <div class="stat-card"><b>5000+</b><span>Homes Powered</span></div>
    <div class="stat-card"><b>£2.5M</b><span>Energy Savings</span></div>
    <div class="stat-card"><b>95%</b><span>Customer Satisfaction</span></div>
  </div>
</section>

<section class="abs about">
  <div class="abs about-text">
    <h2>About Brightvale Energy</h2>
    <p>For over 15 years, we've been pioneering sustainable energy solutions across the UK, helping homeowners transition to clean, renewable power while reducing their energy costs.</p>
    <h3>Our Mission</h3>
    <p>Founded in 2009 with a vision to make renewable energy accessible to every UK household, Brightvale Energy has grown from a small team of passionate engineers to become one of the country's most trusted solar installation companies.</p>
    <a class="btn btn-dark">Read More</a>
  </div>
  <div class="abs about-photo photo" role="img" aria-label="Close view of solar panels under a bright sky"></div>
  <div class="abs badge"><div><small>Projects Completed</small><b>5,000+</b></div><i></i></div>
</section>

<section class="abs solutions">
  <h2 class="section-title" style="margin-top:10px">Complete Renewable Energy<br>Solutions</h2>
  <div class="abs cards">
    <div class="sol-card">
      <div class="img" style="background:linear-gradient(160deg,#d9e6ee,#7d95a8)" role="img" aria-label="House roof fitted with solar panels"></div>
      <h3>Solar PV</h3>
      <p>High-efficiency solar photovoltaic panels that convert sunlight into clean electricity for your home.</p>
      <ul><li><span class="tick"><svg viewBox="0 0 8 8"><path d="M1 4l2 2 4-4" stroke="#fff" fill="none" stroke-width="1.5"/></svg></span>Up to 70% energy savings</li><li><span class="tick"><svg viewBox="0 0 8 8"><path d="M1 4l2 2 4-4" stroke="#fff" fill="none" stroke-width="1.5"/></svg></span>25-year warranty</li><li><span class="tick"><svg viewBox="0 0 8 8"><path d="M1 4l2 2 4-4" stroke="#fff" fill="none" stroke-width="1.5"/></svg></span>Professional installation</li></ul>
      <a class="btn btn-dark">Learn More</a>
    </div>
    <div class="sol-card">
      <div class="img" style="background:linear-gradient(160deg,#eef1f3,#b5bec6)" role="img" aria-label="Wall-mounted home battery units"></div>
      <h3>Battery Energy Storage</h3>
      <p>Store excess solar energy for use when you need it most, reducing grid dependency.</p>
      <ul><li><span class="tick"><svg viewBox="0 0 8 8"><path d="M1 4l2 2 4-4" stroke="#fff" fill="none" stroke-width="1.5"/></svg></span>24/7 backup power</li><li><span class="tick"><svg viewBox="0 0 8 8"><path d="M1 4l2 2 4-4" stroke="#fff" fill="none" stroke-width="1.5"/></svg></span>Smart energy management</li><li><span class="tick"><svg viewBox="0 0 8 8"><path d="M1 4l2 2 4-4" stroke="#fff" fill="none" stroke-width="1.5"/></svg></span>10-year warranty</li></ul>
      <a class="btn btn-dark">Learn More</a>
    </div>
    <div class="sol-card">
      <div class="img" style="background:linear-gradient(160deg,#dfe6ea,#5c7280)" role="img" aria-label="Electric car charging at a home charger"></div>
      <h3>EV Charging</h3>
      <p>Charge your EV with clean solar energy and reduce your transport costs.</p>
      <ul><li><span class="tick"><svg viewBox="0 0 8 8"><path d="M1 4l2 2 4-4" stroke="#fff" fill="none" stroke-width="1.5"/></svg></span>Fast charging speeds</li><li><span class="tick"><svg viewBox="0 0 8 8"><path d="M1 4l2 2 4-4" stroke="#fff" fill="none" stroke-width="1.5"/></svg></span>Smart scheduling</li><li><span class="tick"><svg viewBox="0 0 8 8"><path d="M1 4l2 2 4-4" stroke="#fff" fill="none" stroke-width="1.5"/></svg></span>Solar integration</li></ul>
      <a class="btn btn-dark">Learn More</a>
    </div>
    <div class="sol-card">
      <div class="img" style="background:linear-gradient(160deg,#d3d8db,#3f4a50)" role="img" aria-label="Outdoor heat pump unit beside a house"></div>
      <h3>Heat Pumps</h3>
      <p>Efficient air source heat pumps that provide heating and hot water using renewable energy.</p>
      <ul><li><span class="tick"><svg viewBox="0 0 8 8"><path d="M1 4l2 2 4-4" stroke="#fff" fill="none" stroke-width="1.5"/></svg></span>300% efficiency</li><li><span class="tick"><svg viewBox="0 0 8 8"><path d="M1 4l2 2 4-4" stroke="#fff" fill="none" stroke-width="1.5"/></svg></span>Low running costs</li><li><span class="tick"><svg viewBox="0 0 8 8"><path d="M1 4l2 2 4-4" stroke="#fff" fill="none" stroke-width="1.5"/></svg></span>Government grants available</li></ul>
      <a class="btn btn-dark">Learn More</a>
    </div>
  </div>
</section>

<section class="abs certified">
  <h2>Fully Certified &amp; Accredited</h2>
  <p class="lead">Our commitment to excellence is reflected in our comprehensive certifications and accreditations. We maintain the highest industry standards to ensure quality, safety, and reliability in every installation.</p>
  <div class="chips">
    <div class="chip"><i></i>Microgen Certified Installer</div>
    <div class="chip"><i></i>Electrical Safety Approved Contractor</div>
    <div class="chip"><i></i>QualityMark Government Endorsed</div>
    <div class="chip"><i></i>Consumer Code Member</div>
    <div class="chip"><i></i>Quality Management Standard</div>
    <div class="chip"><i></i>SafeSite Health &amp; Safety Accredited</div>
  </div>
  <h4>Ready to Start <em>Your Renewable Energy Journey?</em></h4>
  <a class="btn btn-lime">Get Free Quote</a>
</section>

<section class="abs values">
  <h2 class="section-title" style="margin-top:20px">Our Core Values</h2>
  <div class="abs value-cards">
    <div class="value"><i></i><h3>Innovation</h3><p>Leading the way with cutting-edge renewable energy technology and smart home integration solutions.</p></div>
    <div class="value"><i></i><h3>Quality</h3><p>Premium products and professional installations backed by comprehensive warranties and certifications.</p></div>
    <div class="value"><i></i><h3>Sustainability</h3><p>Committed to reducing carbon footprints and creating a cleaner, greener future for generations to come.</p></div>
    <div class="value"><i></i><h3>Customer Focus</h3><p>Putting customers first with personalised service, transparent pricing, and ongoing support.</p></div>
  </div>
</section>

<section class="abs why">
  <div class="abs why-photo-a photo" role="img" aria-label="Solar panel array on a residential roof"></div>
  <div class="abs why-photo-b photo" role="img" aria-label="Solar panels in a sunlit field"></div>
  <div class="abs savings"><small>Monthly Savings</small><b>£165</b></div>
  <div class="abs why-text">
    <h2>Why Choose Us?</h2>
    <p>Our mission is to accelerate the UK's transition to renewable energy by providing world-class solar solutions, exceptional customer service.</p>
    <ul>
      <li><span class="tick"><svg viewBox="0 0 8 8"><path d="M1 4l2 2 4-4" stroke="#fff" fill="none" stroke-width="1.5"/></svg></span>Over 15 years of renewable energy expertise</li>
      <li><span class="tick"><svg viewBox="0 0 8 8"><path d="M1 4l2 2 4-4" stroke="#fff" fill="none" stroke-width="1.5"/></svg></span>Certified and fully accredited installations</li>
      <li><span class="tick"><svg viewBox="0 0 8 8"><path d="M1 4l2 2 4-4" stroke="#fff" fill="none" stroke-width="1.5"/></svg></span>Comprehensive 25-year product warranties</li>
      <li><span class="tick"><svg viewBox="0 0 8 8"><path d="M1 4l2 2 4-4" stroke="#fff" fill="none" stroke-width="1.5"/></svg></span>In-house design and installation teams</li>
      <li><span class="tick"><svg viewBox="0 0 8 8"><path d="M1 4l2 2 4-4" stroke="#fff" fill="none" stroke-width="1.5"/></svg></span>Transparent pricing with no hidden costs</li>
      <li><span class="tick"><svg viewBox="0 0 8 8"><path d="M1 4l2 2 4-4" stroke="#fff" fill="none" stroke-width="1.5"/></svg></span>Dedicated customer support throughout your journey</li>
    </ul>
  </div>
</section>

<section class="abs news">
  <h2 class="abs">Latest Energy News</h2>
  <p class="abs intro">Stay informed with the latest developments in renewable energy, government policies, and technological innovations shaping the UK's sustainable future.</p>
  <div class="abs news-cards">
    <div class="news-card"><div class="img" style="background:linear-gradient(160deg,#f3cf86,#6c7f8e)" role="img" aria-label="Solar panels at sunrise"></div><div class="date">15 January 2025</div><h3>UK Government Announces New Solar Panel Grants for 2025</h3><p>Homeowners can now access up to £5,000 in grants for solar panel installations as part of the government's green energy initiative.</p><a>Read More</a></div>
    <div class="news-card"><div class="img" style="background:linear-gradient(160deg,#e3e7ea,#8a97a1)" role="img" aria-label="Rows of battery storage units"></div><div class="date">12 January 2025</div><h3>Battery Storage Costs Drop 40% in 2024</h3><p>Latest market report shows significant cost reductions in home battery storage systems, making renewable energy more accessible.</p><a>Read More</a></div>
    <div class="news-card"><div class="img" style="background:linear-gradient(160deg,#eceff1,#9aa3a8)" role="img" aria-label="Heat pump units outside a home"></div><div class="date">10 January 2025</div><h3>Heat Pump Adoption Accelerates Across the UK</h3><p>New data reveals a 65% increase in heat pump installations as homeowners embrace sustainable heating solutions.</p><a>Read More</a></div>
    <div class="news-card"><div class="img" style="background:linear-gradient(160deg,#d9dee2,#56646e)" role="img" aria-label="Public electric vehicle charging point"></div><div class="date">8 January 2025</div><h3>EV Charging Infrastructure Expansion Plans</h3><p>Major investment announced for home EV charging infrastructure to support the UK's transition to electric vehicles.</p><a>Read More</a></div>
  </div>
  <div class="abs pager">
    <span><svg width="12" height="12" viewBox="0 0 12 12"><path d="M8 2L4 6l4 4" stroke="#173f2b" fill="none" stroke-width="1.6"/></svg></span>
    <span class="on"><svg width="12" height="12" viewBox="0 0 12 12"><path d="M4 2l4 4-4 4" stroke="#fff" fill="none" stroke-width="1.6"/></svg></span>
  </div>
</section>

<section class="abs cta" role="img" aria-label="Green countryside fields under an open sky">
  <h2 class="abs">Ready to Go Solar?</h2>
  <p class="abs lead">Get in touch with our renewable energy experts for a free consultation. We'll help you design the perfect sustainable energy solution for your home.</p>
  <div class="abs contact-panel">
    <div class="contact-item"><i><svg width="14" height="14" viewBox="0 0 14 14"><path d="M3 1h2l1 3-1.5 1a7 7 0 004.5 4.5L10 8l3 1v2a1.5 1.5 0 01-1.5 1.5A10.5 10.5 0 011.5 2.5 1.5 1.5 0 013 1z" fill="#fff"/></svg></i><div><b>Phone</b><span>0800 046 2817</span></div></div>
    <div class="contact-item"><i><svg width="14" height="14" viewBox="0 0 14 14"><path d="M7 1a4 4 0 014 4c0 3-4 8-4 8S3 8 3 5a4 4 0 014-4z" fill="#fff"/><circle cx="7" cy="5" r="1.4" fill="#173f2b"/></svg></i><div><b>Service Areas</b><span>All of England &amp; Wales<br>Local installation teams</span></div></div>
    <div class="contact-item"><i><svg width="14" height="14" viewBox="0 0 14 14"><rect x="1" y="3" width="12" height="8" rx="1" fill="#fff"/><path d="M1 3l6 5 6-5" stroke="#173f2b" fill="none"/></svg></i><div><b>Email</b><span>hello@brightvaleenergy.co.uk</span></div></div>
    <div class="contact-item"><i><svg width="14" height="14" viewBox="0 0 14 14"><circle cx="7" cy="7" r="6" fill="#fff"/><path d="M7 3v4l3 2" stroke="#173f2b" fill="none" stroke-width="1.4"/></svg></i><div><b>Business Hours</b><span>Mon–Fri: 8AM–6PM<br>Saturday: 9AM–4PM</span></div></div>
  </div>
  <div class="abs quote">
    <h3>Get Your Free Quote</h3>
    <p class="sub">Start your renewable energy journey today with a no-obligation consultation.</p>
    <div class="quote-row">Home Energy Assessment<b>FREE</b></div>
    <div class="quote-row">Custom System Design<b>FREE</b></div>
    <div class="quote-row">Installation Quote<b>FREE</b></div>
    <a class="btn">Book Free Consultation</a>
    <p class="rating"><em>★★★★★</em> Average of 4.8/5 stars from 2,000+ customers</p>
  </div>
</section>

<div class="abs statsbar">
  <div><b>5000+</b><span>Homes Powered</span></div>
  <div><b>£2.5M</b><span>Energy Savings</span></div>
  <div><b>95%</b><span>Customer Satisfaction</span></div>
  <div><b>15+</b><span>Year Warranty</span></div>
</div>

<footer class="abs footer">
  <div class="abs footer-brand">
    <div class="logo"><span class="dot"></span>Brightvale Energy</div>
    <p>Leading the UK's transition to renewable energy with premium solar solutions, battery storage and sustainable technologies for residential homes.</p>
    <div class="soc"><span></span><span></span><span></span><span></span></div>
  </div>
  <div class="abs footer-cols">
    <div><h4>Company</h4><ul><li>About Us</li><li>Our Team</li><li>Careers</li><li>News</li></ul></div>
    <div><h4>Products</h4><ul><li>Solar PV</li><li>Battery Storage</li><li>EV Charging</li><li>Heat Pumps</li></ul></div>
    <div><h4>Support</h4><ul><li>Installation Process</li><li>Warranties</li><li>Maintenance</li><li>FAQ</li></ul></div>
    <div><h4>Legal</h4><ul><li>Privacy Policy</li><li>Terms of Service</li><li>Cookie Policy</li><li>Complaints</li></ul></div>
  </div>
  <div class="abs footer-bottom">
    <span>© 2025 Brightvale Energy. All rights reserved.</span>
    <span>Company Registration: 00000000 &nbsp;&nbsp; VAT Number: GB000000000</span>
  </div>
</footer>

</body>
</html>
```